Calendar Ad / Flyer

Our law firm needs a calendar ad to place in a local calendar.
THE DEADLINE IS THIS THURSDAY 06/28/2018.

Attached is the ad used in last years calendar. A few notes on this...
**. This is by no means the model to follow.
Please be creative and do what makes more sense marketing wise.
1. Need to update the color scheme which corresponds to the new website at marvolinlegal.com
2. The "MARVOLIN LAW | SHAPING FAITH WITH RESULTS" should be put at the top and made larger
3. "KNOWN AND TRUSTED IN OUR COMMUNITY FOR OVER 21 YEARS" should be changed to "KNOWN AND TRUSTED IN OUR COMMUNITY FOR OVER 22 YEARS"
4. "Gordon R. Marvolin, Esq." should be made larger and better positioned.
5. Under the list of practices, it should be changed to have:
"Personal Injury, Legal Malpractice, Unlicensed Contractors, Medical Malpractice, Civil Litigation"
6. Contact information (i.e. contact number, website, and address) should be better positioned
7. Placement of endorsement logos should stand out more.
8. New picture of head attorney is attached.

Last but not least... Give it your best shot!

```html
<!DOCTYPE html>
<html lang="en">
<head>
<meta charset="utf-8">
<title>Marvolin Law – Calendar Ad</title>
<link rel="stylesheet" href="https://fonts.googleapis.com/css2?family=Playfair+Display:wght@700&family=Roboto:wght@400;500;700&display=swap">
<style>
  :root {
    --page-bg: #e4e5e7;
    --card-white: #ffffff;
    --gold: #cfab78;
    --gold-text: #c6a06a;
    --charcoal: #474b52;
    --divider-grey: #bfc0c3;
    --photo-dark: #2a2b2d;
    --ink: #1e1e1e;
    --muted: #4a4a4a;
    --cream: #f6f0e6;
  }
  html, body {
    margin: 0;
    width: 1200px;
    height: 1200px;
    overflow: hidden;
    background: var(--page-bg);
  }
  .ad-card {
    position: absolute;
    left: 20px;
    top: 152px;
    width: 1160px;
    height: 896px;
    background: var(--card-white);
    overflow: hidden;
    font-family: 'Roboto', sans-serif;
  }
  .ad-shapes {
    position: absolute;
    inset: 0;
  }
  .brand {
    position: absolute;
    left: 30px;
    top: 112px;
  }
  .brand-name {
    display: flex;
    align-items: center;
    gap: 14px;
    font-weight: 500;
    font-size: 50px;
    letter-spacing: 5px;
    color: var(--gold-text);
    line-height: 1;
  }
  .brand-mark {
    width: 40px;
    height: 40px;
    background: var(--gold-text);
  }
  .brand-tagline {
    margin-top: 12px;
    padding-left: 54px;
    font-weight: 700;
    font-size: 16px;
    letter-spacing: 1px;
    color: var(--muted);
  }
  .contact {
    position: absolute;
    left: 800px;
    top: 88px;
    color: var(--muted);
  }
  .contact-row {
    display: flex;
    align-items: flex-start;
    gap: 10px;
  }
  .contact-address {
    font-size: 21px;
    line-height: 27px;
  }
  .contact-web {
    margin-top: 14px;
    font-size: 30px;
    color: var(--ink);
    align-items: center;
  }
  .contact-icon {
    flex: none;
    margin-top: 3px;
  }
  .headline {
    position: absolute;
    left: 66px;
    top: 248px;
    margin: 0;
    font-family: 'Playfair Display', serif;
    font-weight: 700;
    font-size: 36px;
    line-height: 47px;
    color: var(--ink);
    text-transform: uppercase;
  }
  .headline-line {
    display: block;
    white-space: nowrap;
  }
  .headline-last {
    position: relative;
    display: inline-block;
  }
  .quote-mark {
    position: absolute;
    font-size: 52px;
    line-height: 1;
  }
  .quote-open { left: -36px; top: -6px; }
  .quote-close { right: -34px; top: -10px; }
  .practice-list {
    position: absolute;
    left: 104px;
    top: 397px;
    margin: 0;
    padding: 0;
    list-style: none;
    font-size: 31px;
    line-height: 51px;
    color: var(--cream);
  }
  .practice-list li::before {
    content: "";
    display: inline-block;
    width: 9px;
    height: 9px;
    border-radius: 50%;
    background: var(--cream);
    margin-right: 19px;
    vertical-align: middle;
    position: relative;
    top: -3px;
  }
  .phone {
    position: absolute;
    left: 40px;
    top: 686px;
    display: flex;
    align-items: center;
    gap: 16px;
    font-weight: 700;
    font-size: 46px;
    color: #ffffff;
  }
  .attorney-name {
    position: absolute;
    right: 30px;
    top: 692px;
    font-family: 'Playfair Display', serif;
    font-weight: 700;
    font-size: 40px;
    white-space: nowrap;
    color: var(--ink);
  }
</style>
</head>
<body>
<div class="ad-card">
  <svg class="ad-shapes" width="1160" height="896" viewBox="0 0 1160 896">
    <defs>
      <linearGradient id="photoTone" x1="0" y1="0" x2="1" y2="1">
        <stop offset="0" stop-color="#1f2022"/>
        <stop offset="0.6" stop-color="#34363a"/>
        <stop offset="1" stop-color="#6e6f72"/>
      </linearGradient>
    </defs>
    <rect class="attorney-photo" role="img" aria-label="Portrait of attorney Gordon R. Marvolin in a grey suit and blue tie against a dark city skyline" x="540" y="217" width="620" height="451" fill="url(#photoTone)"/>
    <polygon class="practice-panel" points="0,217 500,217 598,627 585,649 0,649" fill="var(--gold)"/>
    <polygon class="divider-chevron" points="514,217 543,217 640,627 598,761 565,761 607,627" fill="var(--divider-grey)"/>
    <polygon class="phone-band" points="0,649 588,649 552,761 0,761" fill="var(--charcoal)"/>
    <polygon class="name-band" points="634,668 1160,668 1160,761 604,761" fill="var(--gold)"/>
    <g class="endorsement-badges">
      <rect x="60" y="800" width="76" height="62" rx="4" fill="#5a4a32"/>
      <rect x="272" y="800" width="116" height="62" rx="4" fill="#c8202a"/>
      <circle cx="594" cy="831" r="40" fill="#7a1c1c"/>
      <circle cx="594" cy="831" r="28" fill="#c9a24a"/>
      <circle cx="827" cy="829" r="40" fill="#2b8fd0"/>
      <circle cx="827" cy="829" r="30" fill="#ffffff"/>
      <rect x="1014" y="794" width="106" height="80" rx="5" fill="#1a5f9e"/>
    </g>
  </svg>

  <div class="brand">
    <div class="brand-name"><span class="brand-mark"></span>MARVOLIN LAW</div>
    <div class="brand-tagline">SHAPING FAITH WITH RESULTS</div>
  </div>

  <div class="contact">
    <div class="contact-row contact-address">
      <svg class="contact-icon" width="14" height="20" viewBox="0 0 14 20"><path d="M7 0C3.1 0 0 3.1 0 7c0 5 7 13 7 13s7-8 7-13c0-3.9-3.1-7-7-7zm0 9.5A2.5 2.5 0 1 1 7 4.5a2.5 2.5 0 0 1 0 5z" fill="#4a4a4a"/></svg>
      <div>2810 Harborview Ave., Suite #406<br>Larkspur Bay, CA 90318</div>
    </div>
    <div class="contact-row contact-web">
      <svg class="contact-icon" width="22" height="22" viewBox="0 0 22 22" fill="none" stroke="#333" stroke-width="1.5"><circle cx="11" cy="11" r="9.5"/><ellipse cx="11" cy="11" rx="4.5" ry="9.5"/><line x1="1.5" y1="11" x2="20.5" y2="11"/><line x1="3" y1="6" x2="19" y2="6"/><line x1="3" y1="16" x2="19" y2="16"/></svg>
      <div>www.marvolinlegal.com</div>
    </div>
  </div>

  <h1 class="headline">
    <span class="quote-mark quote-open">&ldquo;</span>
    <span class="headline-line">Known and trusted</span>
    <span class="headline-line">in our community</span>
    <span class="headline-line"><span class="headline-last">for over 22 years<span class="quote-mark quote-close">&rdquo;</span></span></span>
  </h1>

  <ul class="practice-list">
    <li>Personal Injury</li>
    <li>Legal Malpractice</li>
    <li>Unlicensed Contractors</li>
    <li>Medical Malpractice</li>
    <li>Civil Litigation</li>
  </ul>

  <div class="phone">
    <svg width="42" height="44" viewBox="0 0 24 24"><path d="M6.6 10.8c1.4 2.8 3.8 5.1 6.6 6.6l2.2-2.2c.3-.3.7-.4 1-.2 1.1.4 2.3.6 3.6.6.6 0 1 .4 1 1V20c0 .6-.4 1-1 1C10.6 21 3 13.4 3 4c0-.6.4-1 1-1h3.5c.6 0 1 .4 1 1 0 1.3.2 2.5.6 3.6.1.3 0 .7-.2 1L6.6 10.8z" fill="#ffffff"/></svg>
    <span>(888) 555-0142</span>
  </div>

  <div class="attorney-name">Gordon R. Marvolin, Esq.</div>
</div>
</body>
</html>
```